Publisher needs book cover for search and rescue book

Book cover needed for book front sized 5.5 x 8.5 inches. About the book: The book is a technical handbook used to instruct either new search and rescue planners involved in the intelligence gathering aspect of a missing person incident or experienced providers who wish to learn new techniques and methods to collect intelligence about a missing person to better plan the field response of where to send resources or identify additional data that needs to be collected. . A background color of navy blue is preferred but open to suggestions. Interested in concepts that suggest collection of intelligence, search and rescue, law enforcement, and should be highly professional in appearance.

Target Market(s)

The target audience for the book is: Search and rescue professionals involved in the collection and analysis of intelligence used to plan where to send resources and law enforcement officers who either look for missing persons or supervise search and rescue resources.

Industry/Entity Type

Search And Rescue

Colors
0455a3

Requirements
Must have
• Title: Quiet Compass
Subtitle: Guiding the Evidence Workflow On the Hunt for Absent Travellers
The author is: Benedict R. Harlow
Image or images that brand the collection of intelligence used in search and rescue/missing persons
Nice to have
• Like the concept of an image of going deeper and deeper which each layer revealing new information.
The author has a concept of a picture that is blurry, one magnify glass reveals what the picture is, a second magnifying glass reveals even greater unexpected finding. Some designers may work with that concept, while I'm open to other designs that synthesize intelligence gathering and search and rescue/law enforcement themes.
Should not have
• No cartoons

```html
<!DOCTYPE html>
<html lang="en">
<head>
<meta charset="utf-8">
<title>Quiet Compass — Benedict R. Harlow</title>
<link rel="stylesheet" href="https://fonts.googleapis.com/css2?family=Cinzel:wght@400;500&display=swap">
<style>
  :root {
    --paper: #ffffff;
    --navy: #1d3a7c;
    --crimson: #b8373a;
    --mist-strong: #3f5c9c;
    --mist-mid: #7d93c4;
    --mist-soft: #d3dbec;
    --lens-edge: #9fb0d6;
  }
  * { margin: 0; padding: 0; box-sizing: border-box; }
  html, body {
    width: 800px;
    height: 1200px;
    overflow: hidden;
    background: var(--paper);
  }
  .cover {
    position: relative;
    width: 800px;
    height: 1200px;
    background: var(--paper);
    font-family: "Cinzel", serif;
    text-align: center;
  }
  .cover-title {
    position: absolute;
    top: 60px;
    left: 0;
    width: 100%;
    color: var(--navy);
    font-weight: 400;
    font-size: 140px;
    line-height: 146px;
    letter-spacing: 2px;
    text-transform: uppercase;
  }
  .title-rule {
    position: absolute;
    top: 374px;
    left: 60px;
    width: 680px;
    height: 3px;
    background: var(--crimson);
  }
  .cover-subtitle {
    position: absolute;
    top: 400px;
    left: 0;
    width: 100%;
    color: var(--crimson);
    font-weight: 400;
    font-size: 32px;
    line-height: 46px;
    letter-spacing: 0.5px;
  }
  .cover-art {
    position: absolute;
    top: 505px;
    left: 110px;
    width: 580px;
    height: 530px;
  }
  .word-cloud {
    position: absolute;
    inset: 0;
    border-radius: 46% 46% 20% 20% / 60% 60% 12% 12%;
    background: radial-gradient(ellipse 55% 55% at 50% 40%,
      var(--mist-strong) 0%, var(--mist-mid) 45%, var(--mist-soft) 80%, var(--paper) 100%);
  }
  .magnifier {
    position: absolute;
    left: 190px;
    top: 100px;
    width: 220px;
    height: 220px;
  }
  .cover-author {
    position: absolute;
    top: 1058px;
    left: 0;
    width: 100%;
    color: var(--crimson);
    font-weight: 400;
    font-size: 36px;
    letter-spacing: 8px;
    text-transform: uppercase;
  }
</style>
</head>
<body>
  <main class="cover">
    <h1 class="cover-title">Quiet<br>Compass</h1>
    <div class="title-rule"></div>
    <p class="cover-subtitle">Guiding the Evidence Workflow<br>On the Hunt for Absent Travellers</p>
    <div class="cover-art">
      <div class="word-cloud" role="img" aria-label="Head-and-shoulders silhouette built from a cloud of small navy words"></div>
      <svg class="magnifier" viewBox="0 0 220 220" aria-hidden="true">
        <line x1="150" y1="150" x2="205" y2="205" stroke="var(--lens-edge)" stroke-width="34" stroke-linecap="round"/>
        <line x1="150" y1="150" x2="205" y2="205" stroke="var(--paper)" stroke-width="28" stroke-linecap="round"/>
        <circle cx="100" cy="100" r="72" fill="none" stroke="var(--lens-edge)" stroke-width="24"/>
        <circle cx="100" cy="100" r="72" fill="none" stroke="var(--paper)" stroke-width="18"/>
      </svg>
    </div>
    <p class="cover-author">Benedict R. Harlow</p>
  </main>
</body>
</html>
```